LTV Business Card

This is a wide-range political consulting firm specializing in high-profile political campaigns. Red should be a predominant color in the business card, since this is a Heartland Party inspired consulting firm, but the word "heartland" will not appear anywhere in any kind of literature. Look has to be clean and crisp. The design should be forward thinking and appropriate for a company that is trying to break away from a traditionally "stodgy" image in politics.

Target Market(s)

potential national political candidates, wealthy donors,

Industry/Entity Type

Political

Contact Information for Business Card

Lionel T. Vardmoor
Political Consultant
438 Ormond Lane NW
#356
Washington, DC 20471

```html
<!DOCTYPE html>
<html lang="en">
<head>
<meta charset="utf-8">
<title>LTV Business Card</title>
<link href="https://fonts.googleapis.com/css2?family=Arimo:wght@700&family=Open+Sans:wght@400&display=swap" rel="stylesheet">
<style>
  :root {
    --backdrop: #1f2b3d;
    --stripe-light: #a5262d;
    --stripe-dark: #7f2a2f;
    --ink: #ffffff;
    --ink-shadow: rgba(40, 6, 8, 0.75);
  }
  html, body {
    margin: 0;
    width: 1200px;
    height: 970px;
    overflow: hidden;
    background: var(--backdrop);
  }
  .business-card {
    position: absolute;
    left: 144px;
    top: 222px;
    width: 911px;
    height: 525px;
    background-color: var(--stripe-dark);
    background-image: linear-gradient(to right, var(--stripe-light) 0 67px, var(--stripe-dark) 67px 134px);
    background-size: 134px 100%;
    background-repeat: repeat-x;
    background-position: -16px 0;
    color: var(--ink);
  }
  .identity {
    position: absolute;
    left: 0;
    right: 0;
    top: 206px;
    text-align: center;
  }
  .identity-inner {
    display: inline-block;
    position: relative;
    left: 12px;
  }
  .person-name {
    margin: 0;
    font-family: "Arimo", Arial, sans-serif;
    font-weight: 700;
    font-size: 48px;
    line-height: 56px;
    letter-spacing: 0.5px;
    text-shadow: 1px 2px 3px var(--ink-shadow);
  }
  .person-title {
    margin: 0;
    padding-right: 29px;
    text-align: right;
    font-family: "Open Sans", Arial, sans-serif;
    font-weight: 400;
    font-size: 17px;
    line-height: 22px;
    margin-top: 2px;
  }
  .address {
    position: absolute;
    left: 0;
    right: 0;
    top: 452px;
    margin: 0;
    text-align: center;
    font-family: "Arimo", Arial, sans-serif;
    font-weight: 700;
    font-size: 25px;
    line-height: 34px;
    padding-left: 10px;
    text-shadow: 1px 1px 2px var(--ink-shadow);
  }
</style>
</head>
<body>
  <div class="business-card">
    <div class="identity">
      <div class="identity-inner">
        <h1 class="person-name">LIONEL T. VARDMOOR</h1>
        <p class="person-title">POLITICAL CONSULTANT</p>
      </div>
    </div>
    <p class="address">438 ORMOND LANE NW #356 WASHINGTON, DC 20471</p>
  </div>
</body>
</html>
```